Marta Belle Designs & Events business card

I need an elegant informative but not busy business card using my logo. We are a florist with high end customers. I am adding a PDF file and a PNG file for those who requested it
Updates

Target Market(s)

Brides, grooms, men purchasing flowers
Ages 20-65

Industry/Entity Type

Florist

Requirements
Must have
• Business info:
Marta Belle Design & Events
www.martabelleevents-sample.com.
555-418-2763

555-418-2763
Nice to have
• Est 1954
may want Pinterest logo, twitter and linkedin and facbook
Should not have
• Clip art or photos

```html
<!DOCTYPE html>
<html lang="en">
<head>
<meta charset="utf-8">
<title>Marta Belle Design &amp; Events — Business Card</title>
<link rel="stylesheet" href="https://fonts.googleapis.com/css2?family=Open+Sans:wght@400;600;700&display=swap">
<style>
  :root {
    --slate-deep: #1c2020;
    --slate-mid: #3a4444;
    --slate-light: #4f5b5b;
    --blush: #f8a5de;
    --blush-soft: #fbb9e6;
    --blush-edge: #fdd3ef;
    --ink: #141616;
  }
  html, body {
    margin: 0;
    padding: 0;
    width: 1200px;
    height: 703px;
    overflow: hidden;
    background: var(--slate-deep);
  }
  .business-card {
    display: block;
    width: 1200px;
    height: 703px;
  }
  .brand-name {
    font-family: "Open Sans", sans-serif;
    font-weight: 600;
    font-size: 54px;
    fill: var(--blush);
  }
  .established {
    font-family: "Open Sans", sans-serif;
    font-weight: 600;
    font-size: 22px;
    fill: var(--blush);
  }
  .contact-line {
    font-family: "Open Sans", sans-serif;
    font-weight: 700;
    font-size: 21px;
    fill: var(--ink);
  }
</style>
</head>
<body>
<svg class="business-card" viewBox="0 0 1200 703" xmlns="http://www.w3.org/2000/svg">
  <defs>
    <radialGradient id="slate-glow" cx="0.62" cy="0.42" r="0.75">
      <stop offset="0" stop-color="var(--slate-light)"/>
      <stop offset="0.55" stop-color="var(--slate-mid)"/>
      <stop offset="1" stop-color="var(--slate-deep)"/>
    </radialGradient>
    <linearGradient id="blush-band" x1="0" y1="0" x2="0" y2="1">
      <stop offset="0" stop-color="var(--blush-soft)"/>
      <stop offset="1" stop-color="var(--blush)"/>
    </linearGradient>
  </defs>

  <rect class="card-background" width="1200" height="703" fill="url(#slate-glow)"/>

  <g class="blush-band">
    <path role="img" aria-label="Pink band with an embossed floral scroll pattern"
          d="M0 345 C 250 440, 520 560, 800 556 C 960 553, 1100 540, 1200 536 L 1200 703 L 0 703 Z"
          fill="url(#blush-band)"/>
    <path class="band-edge" d="M0 345 C 250 440, 520 560, 800 556 C 960 553, 1100 540, 1200 536"
          fill="none" stroke="var(--blush-edge)" stroke-width="2"/>
  </g>

  <g class="brand-block">
    <text class="brand-name" x="577" y="290" text-anchor="middle">Marta Belle Design &amp; Events</text>
    <text class="established" x="848" y="326" text-anchor="middle">Est 1954</text>
  </g>

  <g class="contact-block">
    <text class="contact-line website" x="603" y="368" text-anchor="middle">www.martabelleevents-sample.com</text>
    <text class="contact-line phone" x="603" y="397" text-anchor="middle">T : 555.418.2763</text>
  </g>
</svg>
</body>
</html>
```